Amendment to designs

I have made some changes to the Project overview:

I am uploading some other files and an example of a card that I think will work better.

I would like the card to have watermarked (ever so lightly) in the background the wallpaper that is currently on my website. It can even be in the lightest of shades of the colour on my website so it is hardly noticeable yet just isn't a stark plain background.

Note: all wording except for my name under my photo is to be in the grey colour on my website (the colour of the wording of my statement: In every breath I take.... passionately."

At the top of the card, I would like the following wording centred please:

Halvorsen.com Pty Ltd
Lumen By Odile Varga Pty Ltd
PELU Organics By Sabine Holt Pty Ltd

Then please insert my photo (please note: I don't want the photo boxed or with a border around it unless it looks better and maybe you will need to send a couple of options such that I can visualise?).

Leave a space under the photo and then put:

Odile Varga (my name only is to be in the same green font and colour as my website)
Author, Speaker, Visionary and
Ambassador for Holistic Family Health
leave a space or two and then insert in italics closer to the bottom of the card
Specialising in Certified Organic goodness

On the back of the card, at the top centred can you please put:

In every breath I take
I choose to live my life passionately.
Please make this italics and lets try it in the green colour the same as my name and also if you can send me a sample in the grey colour as per my website.

PO Box 782
Tarrow Bay NSW 1723

T: (please make the T bold) + 61 407295816
E: (please make the E bold) odile@odilevarga.com
odile@lumenbyodilevarga.com
W: (please make the W bold) www.odilevarga.com
www.lumenbyodilevarga.com

If you could then centre and insert the symbols only for Facebook, Twitter, Instagram and youtube that would be great.

Then insert the QR code as supplied.

that would be wonderful if you could get that to me as soon as possible.
many thanks for your assistance, it is greatly appreciated.

Here are the font details:

The font used for my name on my website is Nouvelle Vague and the one used for all the titles on my website is Cantata One. The main content text font is just Helvetica.

Please email me if you have any questions.

Warmest regards
Odile Varga

Industry/Entity Type

Health

Contact Information for Business Card

On the front - the attached image of the "Pewri" venus flower - half over the front of the card and half over the back? (or even 2/3rd's over the front and 1/3rd over the back?). I like to have a background, nearly an "earthy" textured look but as close to white / cream colour as possible (not just a plain background, see attached image with the "crackled" background effect for example - you may wish to use the background on my website but in a white/cream colour?). Please see the colours and font on my website and match please.

Front of card:
Left hand side of card: Venus flower (see attached image)

Right hand side of card:
Odile Varga

Leave a space then underneath my name in italics and smaller font? (possibly?) please put:
In every breath I take, I choose to live my life passionately.
(please see the colours and font on my website and social media platforms and please match as close to as possible my website (note, however, I will take on board your suggestions)

insert a line (maybe?) the image might be most of the left side and the line doesn't apply there, or the image might be on left hand side above the line - I am looking for suggestions on this.
_____________________________________________________________

On right hand side of card (possibly?) or if you think it is best to only have the image above the line and then the following information all underneath the line then possibly have the two sections below (from Managing Director down to ....odilevarga.com) split left hand side under the line and right hand side under the line (await your thoughts please). (If we have the Venus flower half over the front and half over the back, we should be able to have the line along the bottom and all of the below information down to the end of my website address placed under the line?

Managing Director / Author / Speaker
Halvorsen.com Pty Ltd
Varga Brook Lumen Pty Ltd

PO Box 782
Tarrow Bay NSW 1723
ph: 0407295816
e: odile@odilevarga.com
url: www.odilevarga.com

Back of card:

Other companies: pewrimotion.com
pewrijourney.com
lumenbyodilevarga.com
varga-brook.com
vargabrooklumen.com
pewribyodilevarga.com
Please place on the left hand side of the back of the card or wherever you feel it will fit best

Social media sites (please use the icons from my site but not the colour of the icons, just the image and match the icon colour to what you put on the card:

insert Facebook icon then facebook url: https://www.facebook.com/OdileVargaOfficial
https://lumenbyodilevarga

insert Twitter icon then twitter url: https://twitter.com/Odile_Varga

insert Instagram icon then instagram name:
odilevarga
lumenbyodilevarga

insert youtube icon then youtube url:
http://www.youtube.com/channel/UCQ3-HtrPbnJa-wkYxLoRTEs

insert QR code such that people can scan the same and find out about what I do.
QR code has been uploaded

Logo Text

To be in line with my website so that it is consistent

Requirements
Must have
• My image, social media icons,

```html
<!DOCTYPE html>
<html lang="en">
<head>
<meta charset="utf-8">
<title>Odile Varga – Business Card Front</title>
<link rel="stylesheet" href="https://fonts.googleapis.com/css2?family=Encode+Sans+Condensed:wght@300&family=Lato:ital,wght@1,300&display=swap">
<style>
  :root {
    --bg-top: #cdcdd0;
    --bg-bottom: #e7e2c6;
    --brand-green: #1c9a4a;
    --flower-deep: #3f9e55;
    --flower-light: #a6dcbc;
    --text-grey: #3d3d3f;
    --texture-line: rgba(255, 255, 255, 0.14);
  }

  * { margin: 0; padding: 0; box-sizing: border-box; }

  html, body {
    width: 1200px;
    height: 692px;
    overflow: hidden;
  }

  .card {
    position: relative;
    width: 1200px;
    height: 692px;
    overflow: hidden;
    background:
      repeating-linear-gradient(
        180deg,
        transparent 0,
        transparent 3px,
        var(--texture-line) 3px,
        var(--texture-line) 4px
      ),
      linear-gradient(180deg, var(--bg-top) 0%, var(--bg-bottom) 100%);
  }

  .card__flower {
    position: absolute;
    left: 0;
    top: 0;
    width: 520px;
    height: 692px;
  }

  .card__identity {
    position: absolute;
    left: 470px;
    top: 196px;
    width: 690px;
    text-align: center;
  }

  .card__name {
    font-family: "Encode Sans Condensed", "Arial Narrow", sans-serif;
    font-weight: 300;
    font-size: 118px;
    line-height: 1;
    color: var(--brand-green);
    letter-spacing: -1px;
  }

  .card__motto {
    margin-top: 14px;
    font-family: "Lato", "Gill Sans", sans-serif;
    font-style: italic;
    font-weight: 300;
    font-size: 40px;
    line-height: 62px;
    color: var(--text-grey);
  }
</style>
</head>
<body>
  <main class="card">
    <svg class="card__flower" viewBox="0 0 520 692" role="img" aria-label="Venus flower emblem in layered greens">
      <defs>
        <linearGradient id="flowerTone" x1="0" y1="0" x2="1" y2="1">
          <stop offset="0%" stop-color="var(--flower-deep)"/>
          <stop offset="55%" stop-color="var(--flower-light)"/>
          <stop offset="100%" stop-color="var(--flower-deep)"/>
        </linearGradient>
      </defs>
      <rect x="0" y="0" width="520" height="692" fill="url(#flowerTone)"/>
    </svg>

    <section class="card__identity">
      <h1 class="card__name">Odile Varga</h1>
      <p class="card__motto">In every breath I take,<br>I choose to live my life passionately</p>
    </section>
  </main>
</body>
</html>
```